Bright Locker Haven - Free Moving Truck Design

Looking to wrap graphic on 17' box moving truck for my self storage facility based in orange, california. The graphic will need to cover the 4 sides of the box truck, 2 doors and hood. The design should incorporate our business, but must have a wow, look at me factor. The bulk of our customers are residential, live within 5 miles, have disposable income or have an unexpected need to store personal items. We have several commercial accounts, which tend to be our long term customer, which benefits our business. Our facility features: Free Move-In Truck, Individual door alarms, Coded gate access, Month to Month leases, Senior/Military Discounts, Moving & Packing Supplies, knowledgeable & friendly staff. The truck is intended to be a moving billboard when in use.
website: https://www.brightlockerhaven.example/self-storage/ca/orange/dunmore-ave/

Target Market(s)

Apartment dwellers, residential renters, inventory type businesses such as pharmacuticals, construction, plumbing, HVAC, street vendors, home remodelers, college students,

Industry/Entity Type

Self Storage

Colors
FFF300
FFF600
FEFA6F
FFFEC7
FFFEE8
EB3D1F
EC4F4E
F09395
F8D3D4
FCEDEE

Requirements
Must have
• Logo, "We sell boxes", tie in to our Self Storage business, features, phone number 714-555-0147, email address: brightlockerhavenorange.example, address: 517 W. Dunmore Ave., Orange, Ca 82841
Nice to have
• Real people, row of self storage units
Should not have
• Small font, scriptive font

```html
<!DOCTYPE html>
<html lang="en">
<head>
<meta charset="utf-8">
<title>Bright Locker Haven – Truck Wrap</title>
<link rel="stylesheet" href="https://fonts.googleapis.com/css2?family=Roboto:wght@700;900&family=Roboto+Condensed:wght@700&display=swap">
<style>
  :root {
    --yellow: #FFF300;
    --yellow-soft: #FEFA6F;
    --cream: #FFFEC7;
    --cream-light: #FFFEE8;
    --red: #EB3D1F;
    --red-soft: #EC4F4E;
    --orange: #F5A623;
    --ink: #151515;
    --white: #FFFFFF;
    --silver: #D9D9D9;
    --stage: #F1F1F1;
  }
  * { box-sizing: border-box; margin: 0; padding: 0; }
  html, body { width: 1200px; height: 1137px; overflow: hidden; }
  body { background: var(--stage); font-family: "Roboto", Arial, sans-serif; color: var(--ink); position: relative; }

  .panel { position: absolute; overflow: hidden; border: 6px solid var(--silver); }

  /* Side panel */
  .side-panel { left: 40px; top: 40px; width: 1120px; height: 600px;
    background: linear-gradient(180deg, var(--cream-light), var(--cream) 60%, var(--yellow-soft)); }
  .side-panel .bands { position: absolute; inset: 0; }
  .side-phone { position: absolute; left: 28px; top: 14px; font-size: 48px; font-weight: 900; letter-spacing: 1px; }
  .side-logo { position: absolute; left: 40px; top: 140px; width: 440px; display: flex; align-items: center; gap: 22px; }
  .logo-mark { flex: none; width: 70px; height: 70px; background: var(--yellow); border: 5px solid var(--ink); }
  .logo-name { font-family: "Roboto", Arial, sans-serif; font-weight: 900; font-size: 62px; line-height: 0.95; color: var(--ink); text-transform: uppercase; }
  .scene-art { position: absolute; left: 600px; top: 16px; width: 490px; height: 370px; border-radius: 6px;
    background: linear-gradient(135deg, #8ed3e6 0%, #f2e36b 55%, #7a5cc9 100%); }
  .web-strip { position: absolute; left: 0; top: 416px; width: 560px; height: 46px; background: var(--cream-light);
    font-family: "Roboto Condensed", Arial, sans-serif; font-size: 30px; font-weight: 700; padding: 5px 16px; }
  .feature-block { position: absolute; left: 0; top: 462px; width: 560px; height: 126px; background: var(--red);
    color: var(--white); font-family: "Roboto Condensed", Arial, sans-serif; font-size: 25px; font-weight: 700;
    line-height: 30px; padding: 8px 16px; }
  .supplies-strip { position: absolute; right: 0; top: 400px; width: 500px; height: 46px; background: var(--red-soft);
    color: var(--white); font-family: "Roboto Condensed", Arial, sans-serif; font-size: 27px; font-weight: 700;
    text-align: right; padding: 6px 22px; }
  .boxes-callout { position: absolute; right: 22px; top: 462px; display: flex; align-items: center; gap: 14px; }
  .boxes-lead { font-family: "Roboto Condensed", Arial, sans-serif; font-size: 42px; font-weight: 700; color: var(--ink); }
  .boxes-tag { background: var(--red); color: var(--white); font-size: 48px; font-weight: 900; padding: 4px 16px; border: 4px solid var(--white); }
  .address { position: absolute; right: 22px; bottom: 14px; font-family: "Roboto Condensed", Arial, sans-serif;
    font-size: 24px; font-weight: 700; color: var(--ink); }

  /* Front panel */
  .front-panel { left: 40px; top: 690px; width: 440px; height: 400px; background: var(--yellow); }
  .front-panel .bands { position: absolute; inset: 0; }
  .front-text { position: absolute; left: 0; right: 0; top: 30px; text-align: center; }
  .front-phone { font-size: 50px; font-weight: 900; line-height: 60px; }
  .front-web { font-family: "Roboto Condensed", Arial, sans-serif; font-size: 20px; font-weight: 700; margin-top: 18px; }
  .front-mail { font-family: "Roboto Condensed", Arial, sans-serif; font-size: 20px; font-weight: 700; margin-top: 14px; }

  /* Cab door */
  .door-panel { left: 530px; top: 690px; width: 630px; height: 400px;
    background: linear-gradient(160deg, var(--orange) 0%, var(--orange) 55%, var(--yellow-soft) 55%, var(--yellow) 100%); }
  .door-logo { position: absolute; left: 70px; top: 150px; display: flex; align-items: center; gap: 22px; }
  .door-logo .logo-name { font-size: 56px; }
</style>
</head>
<body>

<section class="panel side-panel" aria-label="Truck box side">
  <svg class="bands" viewBox="0 0 1108 588" preserveAspectRatio="none" aria-hidden="true">
    <path d="M0 80 H330 Q380 80 400 120 L590 588 H460 L300 160 Q290 130 260 130 H0 Z" fill="var(--yellow)"/>
    <path d="M0 80 H330 Q380 80 400 120 L590 588" fill="none" stroke="var(--red)" stroke-width="28"/>
    <path d="M560 416 H1108 V588 H600 Z" fill="var(--orange)" opacity="0.9"/>
  </svg>
  <div class="side-phone">714-555-0147</div>
  <div class="side-logo">
    <span class="logo-mark"></span>
    <span class="logo-name">Bright Locker Haven</span>
  </div>
  <div class="scene-art" role="img" aria-label="Illustration of movers carrying a couch from a house into a moving truck"></div>
  <div class="web-strip">brightlockerhavenorange.example</div>
  <div class="feature-block">
    Phone/Online payments • Month to Month<br>
    Free move-in truck • Surveillance Security<br>
    Coded gate access • Individual Door Alarms
  </div>
  <div class="supplies-strip">Moving &amp; Shipping Supplies</div>
  <div class="boxes-callout">
    <span class="boxes-lead">WE SELL</span>
    <span class="boxes-tag">BOXES</span>
  </div>
  <div class="address">517 W. Dunmore Ave., Orange, Ca 82841</div>
</section>

<section class="panel front-panel" aria-label="Truck box front">
  <svg class="bands" viewBox="0 0 428 388" preserveAspectRatio="none" aria-hidden="true">
    <path d="M0 0 H428 V150 Q410 195 360 268 Q338 300 295 300 H133 Q90 300 68 268 Q18 195 0 150 Z" fill="var(--red)"/>
    <path d="M22 0 H406 V145 Q388 185 340 250 Q320 275 285 275 H143 Q108 275 88 250 Q40 185 22 145 Z" fill="var(--cream-light)"/>
  </svg>
  <div class="front-text">
    <div class="front-phone">714-555-0147</div>
    <div class="front-web">brightlockerhavenorange.example</div>
    <div class="front-mail">hello@brightlockerhaven.example</div>
  </div>
</section>

<section class="panel door-panel" aria-label="Cab door">
  <div class="door-logo">
    <span class="logo-mark"></span>
    <span class="logo-name">Bright Locker Haven</span>
  </div>
</section>

</body>
</html>
```